A restaurant needs a new design for menu and presentation flyers.

The name of the restaurant located in Germany is ,, GASTSTÄTTE ZUM MÜHLSTEG" . It means RESTAURANT THE MILL BRIDGE. I attached two photos for reference to see the actual fonts.
I would like to have something close to the fonts we have now. I would like to add a crown representation.Any idea is welcomed.

Target Market(s)

GERMANY

Contact Information for Business Card

Must have ZUM MÜHLSTEG logo.

Requirements
Nice to have
• A crown representation or other symbol who can be representative for our business.
An font close to actual fonts.

```html
<!DOCTYPE html>
<html lang="de">
<head>
<meta charset="utf-8">
<title>Gaststätte Zum Mühlsteg – Menu</title>
<link href="https://fonts.googleapis.com/css2?family=Cabin:wght@400&family=Jost:wght@400;500&family=Libre+Baskerville&family=Oswald:wght@500;700&family=Pinyon+Script&family=Raleway:ital,wght@1,300&family=Josefin+Sans:wght@600&display=swap" rel="stylesheet">
<style>
  :root{
    --slate:#46464f;
    --paper:#ddd5ca;
    --gold:#c8923f;
    --band:#b9843a;
    --ink:#1f1d1b;
    --muted:#6f6963;
    --light:#f1eee8;
  }
  *{margin:0;padding:0;box-sizing:border-box}
  html,body{width:1200px;height:776px;overflow:hidden;background:var(--paper)}
  .spread{position:relative;width:1200px;height:776px;overflow:hidden}

  /* Cover side */
  .cover{position:absolute;left:0;top:0;width:600px;height:776px;background:var(--slate);color:var(--light)}
  .brand{position:absolute;left:0;width:600px;top:296px;text-align:center;
    font-family:"Jost",sans-serif;font-weight:500;font-size:40px;letter-spacing:2px;color:var(--gold)}
  .brand-dot{display:inline-block;width:14px;height:14px;border-radius:50%;background:var(--gold);
    margin-right:14px;vertical-align:middle;position:relative;top:-4px}
  .tagline{position:absolute;left:0;width:620px;top:558px;text-align:center;
    font-family:"Raleway",sans-serif;font-style:italic;font-weight:300;font-size:9.6px;line-height:12.5px;letter-spacing:1px}
  .website{position:absolute;left:0;width:626px;top:638px;text-align:center;
    font-family:"Oswald",sans-serif;font-weight:700;font-size:14px;letter-spacing:5.2px}
  .socials{position:absolute;top:689px;left:0;width:600px;height:16px}
  .social{position:absolute;display:flex;align-items:center;
    font-family:"Josefin Sans",sans-serif;font-weight:600;font-size:10px;letter-spacing:1.6px}
  .social-mark{width:11px;height:11px;border:1.3px solid var(--light);border-radius:50%;margin-right:12px}

  /* Menu side */
  .menu{position:absolute;left:600px;top:0;width:600px;height:776px;background:var(--paper)}
  .menu-title{position:absolute;left:0;width:570px;top:58px;text-align:center;
    font-family:"Pinyon Script",cursive;font-size:68px;color:var(--gold);line-height:1}
  .diamond{position:absolute;top:98px;width:6px;height:6px;background:var(--gold);transform:rotate(45deg)}
  .banner{position:absolute;height:28px;background:var(--band);color:#fff;
    font-family:"Oswald",sans-serif;font-weight:500;font-size:12.5px;line-height:28px;letter-spacing:.2px}
  .banner-main,.banner-side{width:99px;padding-left:12px;clip-path:polygon(0 0,94% 0,100% 100%,0 100%)}
  .banner-main{left:36px;top:204px}
  .banner-side{left:331px;top:204px}
  .banner-drinks{left:222px;top:566px;width:157px;text-align:center;
    clip-path:polygon(0 0,100% 0,97% 50%,100% 100%,0 100%,3% 50%)}
  .divider{position:absolute;left:300px;width:1px;background:#8d8780}
  .divider-food{top:261px;height:264px}
  .divider-drinks{top:626px;height:48px}

  .item{position:absolute;width:240px;height:62px}
  .item-name{font-family:"Jost",sans-serif;font-size:13px;color:var(--ink);letter-spacing:.3px;line-height:16px;white-space:nowrap}
  .item-initial{font-family:"Pinyon Script",cursive;font-size:20px;margin-right:1px}
  .item-desc{margin-top:5px;width:198px;font-family:"Cabin",sans-serif;font-size:9.4px;line-height:12px;color:var(--muted);letter-spacing:.3px;white-space:nowrap;overflow:hidden}
  .item-price{position:absolute;left:209px;top:22px;font-family:"Libre Baskerville",serif;font-size:21px;color:var(--ink)}

  .col-left{left:36px}
  .col-right{left:331px}

  .base-band{position:absolute;left:0;bottom:0;width:600px;height:31px;background:var(--band)}
</style>
</head>
<body>
<div class="spread">

  <section class="cover">
    <h1 class="brand"><span class="brand-dot"></span>ZUM MÜHLSTEG</h1>
    <p class="tagline">Ut enim ad minim veniam, quis nostrud exercitation ullamco.<br>Excepteur sint occaecat cupidatat non proident.</p>
    <p class="website">WWW.RESTAURANTNAME.COM</p>
    <div class="socials">
      <span class="social" style="left:88px"><span class="social-mark"></span>YOUR SOCIAL PAGE</span>
      <span class="social" style="left:264px"><span class="social-mark"></span>YOUR PHOTO FEED</span>
      <span class="social" style="left:412px"><span class="social-mark"></span>YOUR CHAT LINE</span>
    </div>
  </section>

  <section class="menu">
    <span class="diamond" style="left:172px"></span>
    <h2 class="menu-title">Menu</h2>
    <span class="diamond" style="left:388px"></span>

    <div class="banner banner-main">MAIN DISHES</div>
    <div class="banner banner-side">SIDE DISHES</div>
    <div class="divider divider-food"></div>

    <div class="item col-left" style="top:262px"><p class="item-name"><span class="item-initial">S</span>INT OCCAECAT</p><p class="item-desc">Sed ut perspiciatis unde omnis iste natus<br>error sit voluptatem accusantium.................</p><span class="item-price">$5</span></div>
    <div class="item col-left" style="top:335px"><p class="item-name"><span class="item-initial">Q</span>UIS NOSTRUD</p><p class="item-desc">Sed ut perspiciatis unde omnis iste natus<br>error sit voluptatem accusantium.................</p><span class="item-price">$7</span></div>
    <div class="item col-left" style="top:407px"><p class="item-name"><span class="item-initial">E</span>USMOD TEMPOR</p><p class="item-desc">Sed ut perspiciatis unde omnis iste natus<br>error sit voluptatem accusantium.................</p><span class="item-price">$8</span></div>
    <div class="item col-left" style="top:480px"><p class="item-name"><span class="item-initial">L</span>OREM IPSUM</p><p class="item-desc">Sed ut perspiciatis unde omnis iste natus<br>error sit voluptatem accusantium.................</p><span class="item-price">$3</span></div>

    <div class="item col-right" style="top:262px"><p class="item-name"><span class="item-initial">S</span>INT OCCAECAT</p><p class="item-desc">Sed ut perspiciatis unde omnis iste natus<br>error sit voluptatem accusantium.................</p><span class="item-price">$5</span></div>
    <div class="item col-right" style="top:335px"><p class="item-name"><span class="item-initial">Q</span>UIS NOSTRUD</p><p class="item-desc">Sed ut perspiciatis unde omnis iste natus<br>error sit voluptatem accusantium.................</p><span class="item-price">$7</span></div>
    <div class="item col-right" style="top:407px"><p class="item-name"><span class="item-initial">E</span>USMOD TEMPOR</p><p class="item-desc">Sed ut perspiciatis unde omnis iste natus<br>error sit voluptatem accusantium.................</p><span class="item-price">$8</span></div>
    <div class="item col-right" style="top:480px"><p class="item-name"><span class="item-initial">L</span>OREM IPSUM</p><p class="item-desc">Sed ut perspiciatis unde omnis iste natus<br>error sit voluptatem accusantium.................</p><span class="item-price">$3</span></div>

    <div class="banner banner-drinks">DRINKS</div>
    <div class="divider divider-drinks"></div>

    <div class="item col-left" style="top:627px"><p class="item-name"><span class="item-initial">S</span>INT OCCAECAT</p><p class="item-desc">Sed ut perspiciatis unde omnis iste natus<br>error sit voluptatem accusantium.................</p><span class="item-price">$5</span></div>
    <div class="item col-right" style="top:627px"><p class="item-name"><span class="item-initial">S</span>INT OCCAECAT</p><p class="item-desc">Sed ut perspiciatis unde omnis iste natus<br>error sit voluptatem accusantium.................</p><span class="item-price">$5</span></div>

    <div class="base-band"></div>
  </section>

</div>
</body>
</html>
```